Bookmark Design

We would like to design a book mark with logos of our two business and a quote.

One side with the quote "The first wealth is health" - Tobias Quill Harrow and the two logos.

The back side has the two logos with its respective phone numbers and a common address (this is to be advised to the winner of the project).

```html
<!DOCTYPE html>
<html lang="en">
<head>
<meta charset="utf-8">
<title>Bookmark – Northgate Dental &amp; Larkmoor Clinic</title>
<link href="https://fonts.googleapis.com/css2?family=Pinyon+Script&family=Poppins:wght@400;600&display=swap" rel="stylesheet">
<style>
  :root {
    --paper: #f2f6c6;
    --paper-shade: #e6e2b4;
    --maroon: #6a0f19;
    --brand-green: #4f9e44;
    --pin-red: #e8141c;
    --divider: #000000;
  }
  * { box-sizing: border-box; margin: 0; padding: 0; }
  html, body { width: 1200px; height: 810px; overflow: hidden; background: var(--paper); }
  .bookmark { position: relative; width: 1200px; height: 810px; font-family: "Poppins", sans-serif; color: var(--maroon); }
  .side { position: absolute; left: 0; width: 1200px; overflow: hidden; background: var(--paper); }
  .side--front { top: 0; height: 400px; }
  .side--back { top: 410px; height: 400px; }
  .divider { position: absolute; left: 0; top: 400px; width: 1200px; height: 10px; background: var(--divider); }

  .wave-texture { position: absolute; inset: 0; }
  .side--front .wave-texture { background: radial-gradient(ellipse 70% 45% at 35% 95%, var(--paper-shade), transparent 70%), linear-gradient(160deg, var(--paper-shade) 0%, transparent 35%); opacity: .8; }
  .side--back .wave-texture { background: radial-gradient(ellipse 70% 40% at 60% 100%, var(--paper-shade), transparent 70%), linear-gradient(200deg, var(--paper-shade) 0%, transparent 35%); opacity: .8; }

  .brand { position: absolute; display: flex; align-items: center; gap: 6px; font-weight: 600; color: var(--brand-green); line-height: 1.1; }
  .brand__dot { width: 14px; height: 14px; border-radius: 50%; background: var(--brand-green); flex: none; }

  .front-brands .brand--dental { left: 978px; top: 42px; font-size: 15px; }
  .front-brands .brand--clinic { left: 1100px; top: 42px; font-size: 15px; }

  .quote { position: absolute; left: 0; width: 1200px; top: 160px; text-align: center; font-family: "Pinyon Script", cursive; font-size: 84px; font-weight: 400; -webkit-text-stroke: 1.2px var(--maroon); color: var(--maroon); padding-left: 20px; }
  .quote-author { position: absolute; right: 82px; top: 255px; font-family: "Pinyon Script", cursive; font-size: 34px; -webkit-text-stroke: .6px var(--maroon); }

  .contact { position: absolute; font-size: 14px; line-height: 16.5px; color: var(--maroon); }
  .back-brands .brand--clinic { left: 38px; top: 78px; font-size: 17px; }
  .contact--clinic { left: 194px; top: 76px; }
  .heart-ornament { position: absolute; left: 435px; top: 180px; width: 320px; height: 67px; border-radius: 50%; background: radial-gradient(ellipse at center, rgba(106,15,25,.35), rgba(106,15,25,0) 70%); }
  .pin { position: absolute; left: 37px; top: 307px; width: 46px; height: 60px; }
  .contact--address { left: 100px; top: 318px; }
  .contact--dental { right: 211px; top: 318px; text-align: right; }
  .back-brands .brand--dental { left: 1020px; top: 325px; font-size: 17px; }
</style>
</head>
<body>
<main class="bookmark">
  <section class="side side--front">
    <div class="wave-texture" role="img" aria-label="Fine flowing wave line pattern in soft beige"></div>
    <div class="front-brands">
      <div class="brand brand--dental"><span class="brand__dot"></span>Northgate<br>Dental</div>
      <div class="brand brand--clinic">Larkmoor<br>Clinic</div>
    </div>
    <h1 class="quote">The first wealth is health</h1>
    <p class="quote-author">-Tobias Quill Harrow</p>
  </section>

  <div class="divider"></div>

  <section class="side side--back">
    <div class="wave-texture" role="img" aria-label="Fine flowing wave line pattern in soft beige"></div>
    <div class="back-brands">
      <div class="brand brand--clinic"><span class="brand__dot"></span>Larkmoor<br>Clinic</div>
      <div class="brand brand--dental"><span class="brand__dot"></span>Northgate<br>Dental</div>
    </div>
    <p class="contact contact--clinic">Contact:<br>detailsdetailsdetailsdetailsdetails<br>detailsdetailsdetailsdetailsdetails</p>
    <div class="heart-ornament" role="img" aria-label="Maroon brush swashes with a heartbeat heart ornament"></div>
    <svg class="pin" viewBox="0 0 46 60" aria-hidden="true">
      <path d="M23 0C10 0 0 10 0 23c0 15 23 37 23 37s23-22 23-37C46 10 36 0 23 0z" fill="var(--pin-red)"/>
      <circle cx="23" cy="21" r="8" fill="#ffffff"/>
    </svg>
    <p class="contact contact--address">detailsdetailsdetailsdetailsdetails<br>detailsdetailsdetailsdetailsdetails<br>detailsdetailsdetailsdetailsdetails</p>
    <p class="contact contact--dental">Contact:<br>detailsdetailsdetailsdetailsdetails<br>detailsdetailsdetailsdetailsdetails</p>
  </section>
</main>
</body>
</html>
```